Health Coach needs a Business Card Design

Need a really modern feminine business card design for a health and lifestyle coach. Needs to use geometric shapes, muted grey/blue/green pastels and black and white - see mood board attached and logo. The client likes black and white, modern, san serif with the use of lines and possibly a shadow leaf as in the mood board. Possibly put the tag line on the back or an icon of the logo. Logo is also attached. An icon of the logo would be great too.

Target Market(s)

Women (some men) aged 30 to 50.

Industry/Entity Type

Business

Contact Information for Business Card

Maren Tolvey
e-mail: hello@marentwell.net
website: marentwell.net
Phone: +610497268153

The tag line is "A balanced body for Life"

Font styles to use
Sans Serif

Colors
ecf7fb
cfeae6
000000
ffffff
f5f5f5

Requirements
Must have
• Black and white, logo, tag line and details
Nice to have
• Would be nice to incorporate the shadow palm.fern leaves as in the mood board and or geometric lines/shapes - see mood board. Could be either standard rectangle or would be happy with square too.
Should not have
• Flowers or decorations

```html
<!DOCTYPE html>
<html lang="en">
<head>
<meta charset="utf-8">
<title>Maren Tolvey – Business Card</title>
<link rel="stylesheet" href="https://fonts.googleapis.com/css2?family=Jost:wght@400;500&display=swap">
<style>
  :root {
    --backdrop: #ecece9;
    --card-blue: #b4c8d3;
    --ink: #111111;
  }
  * { margin: 0; padding: 0; box-sizing: border-box; }
  html, body {
    width: 966px;
    height: 1200px;
    overflow: hidden;
    background: var(--backdrop);
  }
  .canvas {
    position: relative;
    width: 966px;
    height: 1200px;
    font-family: "Jost", "Helvetica Neue", Arial, sans-serif;
    color: var(--ink);
  }
  .card {
    position: absolute;
    left: 206px;
    width: 555px;
    height: 345px;
    background: var(--card-blue);
  }
  .card--front { top: 135px; }
  .card--back { top: 771px; }

  /* Front */
  .contact-block {
    position: absolute;
    top: 134px;
    left: 0;
    width: 100%;
    text-align: center;
  }
  .contact-block__name {
    font-size: 23px;
    font-weight: 400;
    letter-spacing: 0.03em;
    line-height: 1;
    text-transform: uppercase;
  }
  .contact-block__details {
    display: inline-block;
    margin-top: 8px;
    padding: 3px 2px 4px;
    border-top: 1px solid var(--ink);
    border-bottom: 1px solid var(--ink);
    font-size: 13px;
    line-height: 1.2;
    white-space: nowrap;
  }
  .contact-block__label { font-weight: 500; }
  .contact-block__gap { display: inline-block; width: 10px; }
  .contact-block__web {
    margin-top: 6px;
    font-size: 13.5px;
    font-weight: 500;
    letter-spacing: 0.12em;
    text-transform: uppercase;
  }

  /* Back */
  .brand-block {
    position: absolute;
    top: 128px;
    left: 142px;
    width: 320px;
    text-align: center;
  }
  .brand-block__name {
    font-size: 34px;
    font-weight: 400;
    letter-spacing: 0.04em;
    line-height: 1;
  }
  .brand-block__tagline {
    margin-top: 18px;
    font-size: 14px;
    font-weight: 400;
    letter-spacing: 0.2em;
    text-transform: uppercase;
    white-space: nowrap;
  }
</style>
</head>
<body>
<main class="canvas">
  <section class="card card--front" aria-label="Card front">
    <div class="contact-block">
      <h1 class="contact-block__name">Maren Tolvey</h1>
      <p class="contact-block__details">
        <span class="contact-block__label">P:</span> +610497268153<span class="contact-block__gap"></span><span class="contact-block__label">E:</span> hello@marentwell.net
      </p>
      <p class="contact-block__web">www.marentwell.net</p>
    </div>
  </section>

  <section class="card card--back" aria-label="Card back">
    <div class="brand-block">
      <p class="brand-block__name">Maren T</p>
      <p class="brand-block__tagline">A balanced body for life</p>
    </div>
  </section>
</main>
</body>
</html>
```